business card design for a small scale specialty cut flower farm

We need a business card design for Hollowmere Bloom Farm based in Langley, BC, Canada. We produce specialty, high-end cut flowers and sell locally to florists, local shops and markets and the end user through bouquet subscriptions. The final business card design should be memorable and have a timeless or vintage feel. We would prefer a square shape.
Updates

Target Market(s)

florists, shops and seasonal markets, local flower lovers

Industry/Entity Type

Floral

Contact Information for Business Card

Tamsin Ellery Voss, Grower
Langley, BC, Canada
website: hollowmerebloomfarm.example
instagram: @hollowmerebloomfarm
Tel: 555.317.4290
facebook: www.facebook.example/hollowmereblooms/

Font styles to use
Serif
Decorative
Script

Requirements
Must have
• soft black background colour on front side, the included logo and catch phrase: Fresh Local Seasonal
Nice to have
• phone number and website address on front of card, included photo 6539 incorporated onto the back, possibly photo 6609 as well.

```html
<!DOCTYPE html>
<html lang="en">
<head>
<meta charset="utf-8">
<title>Hollowmere Bloom Farm – Business Cards</title>
<link rel="stylesheet" href="https://fonts.googleapis.com/css2?family=Jost:wght@400;500&display=swap">
<style>
  :root {
    --page: #eeebe7;
    --card: #fbfbfa;
    --soft-black: #1e0e09;
    --cocoa: #4b3427;
    --ink: #1b1210;
    --bloom: #f1c6d8;
    --shadow: rgba(30, 14, 9, 0.18);
  }
  * { box-sizing: border-box; margin: 0; padding: 0; }
  html, body {
    width: 1200px;
    height: 900px;
    overflow: hidden;
    background: var(--page);
    font-family: "Jost", sans-serif;
    color: var(--ink);
  }
  .sheet {
    width: 1200px;
    height: 900px;
    display: flex;
    flex-direction: column;
    align-items: center;
    justify-content: center;
    gap: 44px;
  }
  .card {
    position: relative;
    width: 600px;
    height: 386px;
    background: var(--card);
    box-shadow: 0 10px 28px var(--shadow);
    overflow: hidden;
  }
  .card__wave {
    position: absolute;
    inset: 0;
    width: 100%;
    height: 100%;
  }
  .wave__back { fill: var(--cocoa); }
  .wave__front { fill: var(--soft-black); }

  .brand {
    display: flex;
    flex-direction: column;
    align-items: center;
    text-align: center;
  }
  .brand__mark {
    border-radius: 50%;
    background: var(--bloom);
  }
  .brand__name {
    display: flex;
    flex-direction: column;
    font-weight: 400;
    letter-spacing: 0.12em;
    text-transform: uppercase;
    line-height: 1.15;
    white-space: nowrap;
  }
  .brand__tagline,
  .brand__est {
    font-weight: 400;
    letter-spacing: 0.04em;
  }
  .brand__est { letter-spacing: 0.3em; }

  /* Back side: contact list */
  .card--contact .brand {
    position: absolute;
    left: 150px;
    top: 30px;
    width: 200px;
  }
  .card--contact .brand__mark { width: 30px; height: 30px; margin-bottom: 6px; }
  .card--contact .brand__name { font-size: 12px; }
  .card--contact .brand__tagline { font-size: 9px; margin-top: 2px; }
  .card--contact .brand__est { font-size: 7px; margin-top: 2px; }

  .contact-list {
    position: absolute;
    left: 56px;
    top: 176px;
    list-style: none;
    display: flex;
    flex-direction: column;
    gap: 14px;
  }
  .contact-list__item {
    display: flex;
    align-items: center;
    gap: 16px;
    font-size: 17px;
    letter-spacing: 0.03em;
    white-space: nowrap;
  }
  .contact-icon {
    width: 30px;
    height: 30px;
    flex: none;
  }
  .contact-icon__disc { fill: var(--soft-black); }
  .contact-icon__glyph { fill: none; stroke: #fff; stroke-width: 1.6; stroke-linecap: round; }
  .contact-icon__solid { fill: #fff; }

  /* Front side: owner */
  .card--owner .brand {
    position: absolute;
    left: 80px;
    top: 36px;
    width: 300px;
  }
  .card--owner .brand__mark { width: 66px; height: 66px; margin-bottom: 12px; }
  .card--owner .brand__name { font-size: 20px; }
  .card--owner .brand__tagline { font-size: 13px; margin-top: 4px; }
  .card--owner .brand__est { font-size: 10px; margin-top: 6px; }

  .owner {
    position: absolute;
    left: 80px;
    top: 258px;
    width: 300px;
    text-align: center;
    line-height: 1.05;
    white-space: nowrap;
  }
  .owner__role { font-size: 32px; font-weight: 400; letter-spacing: 0.02em; }
  .owner__name { font-size: 24px; font-weight: 400; }
</style>
</head>
<body>
<main class="sheet">

  <section class="card card--contact" aria-label="Card back with contact details">
    <svg class="card__wave" viewBox="0 0 600 386" preserveAspectRatio="none" aria-hidden="true">
      <path class="wave__back" d="M400 0 C375 40 400 80 455 110 C525 150 540 190 495 225 C440 262 405 300 405 386 L600 386 L600 0 Z"/>
      <path class="wave__front" d="M425 0 C402 40 428 80 480 110 C550 150 562 195 520 230 C465 268 432 305 432 386 L600 386 L600 0 Z"/>
    </svg>

    <div class="brand">
      <span class="brand__mark" role="img" aria-label="Hollowmere Bloom Farm flower emblem"></span>
      <span class="brand__name"><span>Hollowmere Bloom</span><span>Farm</span></span>
      <span class="brand__tagline">Specialty Cut Flowers</span>
      <span class="brand__est">EST. 2019</span>
    </div>

    <ul class="contact-list">
      <li class="contact-list__item">
        <svg class="contact-icon" viewBox="0 0 34 34" aria-hidden="true">
          <circle class="contact-icon__disc" cx="17" cy="17" r="17"/>
        </svg>
        <span>/hollowmerebloomfarm</span>
      </li>
      <li class="contact-list__item">
        <svg class="contact-icon" viewBox="0 0 34 34" aria-hidden="true">
          <circle class="contact-icon__disc" cx="17" cy="17" r="17"/>
          <path class="contact-icon__solid" d="M12 9.5 l3 0 l1.2 4 l-2 1.6 c1 2.2 2.5 3.7 4.7 4.7 l1.6 -2 l4 1.2 l0 3 c0 1 -0.8 1.8 -1.8 1.8 C15.5 23.8 10.2 18.5 10.2 11.3 c0 -1 0.8 -1.8 1.8 -1.8 Z"/>
        </svg>
        <span>(555) 317-4290</span>
      </li>
      <li class="contact-list__item">
        <svg class="contact-icon" viewBox="0 0 34 34" aria-hidden="true">
          <circle class="contact-icon__disc" cx="17" cy="17" r="17"/>
          <circle class="contact-icon__glyph" cx="17" cy="17" r="8"/>
          <ellipse class="contact-icon__glyph" cx="17" cy="17" rx="3.5" ry="8"/>
          <path class="contact-icon__glyph" d="M9 17 H25 M10.5 13 H23.5 M10.5 21 H23.5"/>
        </svg>
        <span>hollowmerebloomfarm.example</span>
      </li>
      <li class="contact-list__item">
        <svg class="contact-icon" viewBox="0 0 34 34" aria-hidden="true">
          <circle class="contact-icon__disc" cx="17" cy="17" r="17"/>
        </svg>
        <span>/hollowmereblooms/</span>
      </li>
    </ul>
  </section>

  <section class="card card--owner" aria-label="Card front with owner name">
    <svg class="card__wave" viewBox="0 0 600 386" preserveAspectRatio="none" aria-hidden="true">
      <path class="wave__back" d="M440 0 C400 30 400 90 430 150 C460 210 465 240 430 265 C390 295 372 330 376 386 L600 386 L600 0 Z"/>
      <path class="wave__front" d="M470 0 C432 32 434 92 462 152 C492 212 494 245 458 270 C420 298 402 332 406 386 L600 386 L600 0 Z"/>
    </svg>

    <div class="brand">
      <span class="brand__mark" role="img" aria-label="Hollowmere Bloom Farm flower emblem"></span>
      <span class="brand__name"><span>Hollowmere Bloom</span><span>Farm</span></span>
      <span class="brand__tagline">Specialty Cut Flowers</span>
      <span class="brand__est">EST. 2019</span>
    </div>

    <div class="owner">
      <p class="owner__role">OWNER</p>
      <p class="owner__name">Tamsin Ellery Voss</p>
    </div>
  </section>

</main>
</body>
</html>
```